Tech Savy small Business accountant business card design

We need a business card for a new company based in the cloud. We provide tax, business advisory, accounting, information technology solutions and back office functions to small businesses. We offer fixed fee packages with add on services as you need them. By harnessing technology we simplify small business operational processes providing valuable time and information for small business owners to grow their business. In the logo (zulvarine) we want to be able to see zulv and experts. The final design should communicate achieving growth dreams and balance (ie life and $).
Updates
This project has been temporarily placed on hold until I finalize "Tech Savy small Business accountant needs a logo". I invite all designers to submit on this logo project. Once my logo is finalized I will resume this business card contest. Thanks Added Wednesday, March 19, 2014
This project has been temporarily placed on hold until I finalize "Tech Savy small Business accountant logo". I invite all designers to submit on this logo project. Once my logo is finalized I will resume this business card contest. Thanks Added Thursday, March 20, 2014
Target Market(s)
Small Business (Revenue $500,000, more than 3 employees) owners.
Industry/Entity Type
Small Business
Contact Information for Business Card
Marla Pennick (Principal)
Accountant, Tax Agent.
TEL | 0417 583 916
EMAIL | Marla.Pennick@zulvarine.com.au
WEB | www.zulvarine.com.au
Look and feel

```html
<!DOCTYPE html>
<html lang="en">
<head>
<meta charset="utf-8">
<title>zulvarine business card</title>
<link href="https://fonts.googleapis.com/css2?family=Open+Sans:wght@400;600;700&display=swap" rel="stylesheet">
<style>
  :root {
    --page-bg: #eceef0;
    --card-white: #ffffff;
    --brand-blue: #1f8fd6;
    --brand-blue-deep: #1668b8;
    --brand-blue-light: #5cc4ee;
    --pale-blue: #e3f1fa;
    --soft-grey: #e3e5e8;
    --text-grey: #7d7f82;
    --shadow: rgba(20, 40, 70, 0.18);
  }
  * { box-sizing: border-box; margin: 0; padding: 0; }
  html, body {
    width: 1200px; height: 913px; overflow: hidden;
    background: var(--page-bg);
    font-family: "Open Sans", Arial, sans-serif;
  }
  .canvas {
    position: relative; width: 1200px; height: 913px;
    display: flex; flex-direction: column; align-items: center; justify-content: center; gap: 48px;
  }
  .card {
    position: relative; width: 620px; height: 354px;
    border-radius: 18px; overflow: hidden;
    box-shadow: 0 10px 28px var(--shadow);
  }
  /* Front */
  .card-front { background: var(--card-white); }
  .card-front .shapes { position: absolute; inset: 0; }
  .front-content {
    position: absolute; right: 44px; top: 28px;
    text-align: right; color: var(--brand-blue);
  }
  .wordmark { font-weight: 700; letter-spacing: -1px; line-height: 1.05; }
  .card-front .wordmark { font-size: 46px; color: var(--brand-blue); }
  .tagline { font-size: 13px; color: var(--text-grey); line-height: 1.4; }
  .person { margin-top: 16px; }
  .person-name { font-size: 21px; font-weight: 700; color: var(--brand-blue); text-transform: uppercase; line-height: 1.35; }
  .person-role { font-size: 13px; color: var(--text-grey); line-height: 1.4; }
  .contacts { margin-top: 14px; list-style: none; font-size: 13px; line-height: 1.55; }
  .contacts li { display: flex; justify-content: flex-end; align-items: center; gap: 8px; }
  .contacts svg { width: 12px; height: 12px; stroke: var(--text-grey); fill: none; stroke-width: 1.6; flex: none; }
  /* Back */
  .card-back {
    background: linear-gradient(150deg, var(--brand-blue-light) 0%, var(--brand-blue) 50%, var(--brand-blue-deep) 100%);
  }
  .back-content { position: absolute; left: 230px; top: 118px; color: var(--card-white); }
  .card-back .wordmark { font-size: 64px; color: var(--card-white); }
  .card-back .tagline { font-size: 17px; color: var(--card-white); margin-top: 4px; }
  .back-accent {
    position: absolute; left: -60px; bottom: -90px; width: 240px; height: 240px;
    border-radius: 50%; background: rgba(255, 255, 255, 0.08);
  }
</style>
</head>
<body>
<main class="canvas">
  <section class="card card-front" aria-label="Card front">
    <svg class="shapes" viewBox="0 0 620 354" preserveAspectRatio="none" aria-hidden="true">
      <defs>
        <linearGradient id="bandBlue" x1="0" y1="0" x2="1" y2="1">
          <stop offset="0" stop-color="#5cc4ee"/>
          <stop offset="1" stop-color="#1668b8"/>
        </linearGradient>
      </defs>
      <path d="M470 0 L620 0 L620 90 Q570 70 540 30 Z" fill="var(--pale-blue)"/>
      <path d="M0 220 L60 236 L110 354 L0 354 Z" fill="var(--soft-grey)"/>
      <path d="M140 0 L245 0 L285 250 L620 322 L620 354 L230 354 L195 290 Z" fill="url(#bandBlue)"/>
    </svg>
    <div class="front-content">
      <div class="wordmark">zulvarine</div>
      <p class="tagline">Your business and accounting partner</p>
      <div class="person">
        <p class="person-name">Marla Pennick (Principal)</p>
        <p class="person-role">Accountant, Tax Agent</p>
      </div>
      <ul class="contacts">
        <li>0417 583 916
          <svg viewBox="0 0 16 16"><path d="M4 1.5 L6.5 5 L5 6.5 Q6.5 9.5 9.5 11 L11 9.5 L14.5 12 L12.5 14.5 Q5 13.5 1.5 3.5 Z"/></svg>
        </li>
        <li>www.zulvarine.com.au
          <svg viewBox="0 0 16 16"><circle cx="8" cy="8" r="6.5"/><path d="M1.5 8 H14.5 M8 1.5 Q4 8 8 14.5 M8 1.5 Q12 8 8 14.5"/></svg>
        </li>
        <li>Marla.Pennick@zulvarine.com.au
          <svg viewBox="0 0 16 16"><rect x="1.5" y="3.5" width="13" height="9"/><path d="M1.5 3.5 L8 9 L14.5 3.5"/></svg>
        </li>
      </ul>
    </div>
  </section>

  <section class="card card-back" aria-label="Card back">
    <div class="back-accent" aria-hidden="true"></div>
    <div class="back-content">
      <div class="wordmark">zulvarine</div>
      <p class="tagline">Your business and accounting partner</p>
    </div>
  </section>
</main>
</body>
</html>
```